Brent Oakes Director / Photographer Branding

I need note pads, envelops, business cards and letter head for my company. I'm a fashion and advertising director / photographer. I'm having trouble deciding how to include both Director & Photographer in my title or if it is even necessary. Maybe just my name is enough. I'm open for even using my initials if it works with the design and overall pieces. Please view my website to see what I have at this moment and what work I do. www.brentoakesstudio-mail.net
Updates

Project Deadline Extended
Reason: Hello Everyone! I'm extending the deadline since I have been traveling on a job out of country and I wanted to have more time to look through all the designs and give enough time for everyone to provide changes with designs and updates. I will be more available to communicate online now that I'm back in the office! Thank you! Brent Oakes

Target Market(s)

Fashion magazines, clothing lines and beauty cosmetic brands.

Industry/Entity Type

Fashion Photography

Font styles to use
Sans Serif

Colors
acd036
acd35d
cbcbcb
f5f5f5

Requirements
Must have
• My name.. Brent Oakes, my website: brentoakesstudio-mail.net my phone number, 555-284-6103
• I don't need my address on these. I also live by the philosophy that less is more and keeping things simple ads strength to a design. I also don't want to stop people from taking chances and experimenting with an idea that might take me down different road with my branding.
Nice to have
• Bold designs and clean lines. I'm open to ideas that I could adopt but I lean towards a more minimalistic look in general.
Should not have
• Not have cheesy graphics or pictures. No images of cameras, film or anything that looks like it is a camera or aperture, lens etc... ;)

```html
<!DOCTYPE html>
<html lang="en">
<head>
<meta charset="utf-8">
<title>Brent Oakes — Letterhead</title>
<link rel="stylesheet" href="https://fonts.googleapis.com/css2?family=Montserrat:wght@400;600&display=swap">
<style>
  :root {
    --backdrop: #dfe2e3;
    --paper: #ffffff;
    --brand-green: #5cf23a;
    --ink: #2b2b2b;
  }
  * { margin: 0; padding: 0; box-sizing: border-box; }
  html, body { width: 1200px; height: 836px; overflow: hidden; }
  body { background: var(--backdrop); position: relative; font-family: "Montserrat", sans-serif; color: var(--ink); }

  .sheet { position: absolute; width: 362px; height: 512px; background: var(--paper); }
  .sheet--sidebar { left: 201px; top: 128px; }
  .sheet--classic { left: 651px; top: 127px; }

  .name-mark { position: absolute; font-family: "Montserrat", sans-serif; font-weight: 400; color: var(--brand-green); font-size: 13px; line-height: 16px; white-space: nowrap; }
  .sheet--sidebar .name-mark { left: 45px; top: 86px; }
  .sheet--classic .name-mark { left: 46px; top: 52px; }

  .site-link { position: absolute; left: 48px; top: 129px; font-size: 5.6px; color: var(--brand-green); }
  .social-dots { position: absolute; left: 48px; top: 140px; display: flex; gap: 5.5px; }
  .social-dots i { width: 8px; height: 8px; border-radius: 50%; background: var(--brand-green); display: block; }

  .letter-body { position: absolute; font-size: 6.3px; text-align: justify; }
  .letter-body p:first-child { text-indent: 22px; }
  .sheet--sidebar .letter-body { left: 140px; top: 72px; width: 181px; line-height: 11.4px; }
  .sheet--sidebar .letter-body p { margin-bottom: 9px; }
  .sheet--classic .letter-body { left: 46px; top: 113px; width: 274px; line-height: 11.6px; }
  .sheet--classic .letter-body p { margin-bottom: 11px; }

  .sign-off { position: absolute; font-size: 6.1px; line-height: 11.5px; }
  .sheet--sidebar .sign-off { left: 199px; top: 347px; text-align: center; }
  .sheet--classic .sign-off { left: 46px; top: 321px; }

  .contact-stack { position: absolute; left: 44px; top: 407px; font-size: 5.6px; font-weight: 600; line-height: 12px; }
  .contact-stack::before { content: ""; display: block; width: 8px; height: 2px; background: var(--brand-green); margin-bottom: 2px; }

  .contact-row { position: absolute; left: 0; width: 100%; top: 440px; display: flex; justify-content: center; gap: 6px; font-size: 5.4px; font-weight: 600; padding-left: 22px; }
  .contact-row span { display: flex; align-items: center; gap: 2.5px; }
  .contact-row i { width: 4px; height: 4px; background: var(--brand-green); display: block; }
  .contact-row svg { width: 5px; height: 5px; }
</style>
</head>
<body>

<section class="sheet sheet--sidebar">
  <div class="name-mark">Brent Oakes</div>
  <div class="site-link">www.brentoakesstudio-mail.net</div>
  <div class="social-dots"><i></i><i></i><i></i><i></i><i></i></div>

  <div class="letter-body">
    <p>Nullam convallis sapien vitae ligula volutpat efficitur. Aliquam quis quam eget ligula sagittis congue id eget felis nullam convallis sapien vitae ligula volutpat efficitur. Aliquam quis quam eget ligula sagittis congue.</p>
    <p>Lorem ipsum dolor sit amet, consectetur adipiscing elit. Nunc bibendum ultricies mi. Duis ac ligula lorem. Nunc ac dui dignissim, facilisis libero sed, posuere mi. Donec suscipit elementum odio. Sed elementum leo diam, a imperdiet quam lobortis nec. Nunc dictum malesuada mi, sed hendrerit lacus aliquet dictum. In iaculis augue at cursus consectetur lis sapien vitae ligula volutpat efficitur. Aliquam quis quam eget ligula sagittis congue.</p>
    <p>Nam mollis ipsum sapien, vehicula fringilla erat fermentum id. Aenean nec feugiat ex. Nunc imperdiet non ligula vitae aliquet. Aliquam pellentesque nec ligula sit amet blandit. Integer vitae aliquet ante. Proin tempor auctor etus ac augue porttitor ornare id et arcu. Aliquam erat volutpat. Nullam convallis sapien vitae ligissim, facilisis libero sed, posuere mi. Donec suscipit elementum odio. Sed elementum leo diam, a imperdiet quam lobortis necunc malesuada mised.</p>
  </div>
  <div class="sign-off">Sincerely,<br>Managing Director</div>

  <div class="contact-stack">
    P. +555-284-6103<br>
    brent@brentoakesstudio-mail.net<br>
    brentoakesstudio-mail.net
  </div>
</section>

<section class="sheet sheet--classic">
  <div class="name-mark">Brent Oakes</div>

  <div class="letter-body">
    <p>Nullam convallis sapien vitae ligula volutpat efficitur. Aliquam quis quam eget ligula sagittis congue id eget felis nullam convallis sapien vitae ligula volutpat efficitur. Aliquam quis quam eget ligula sagittis congue.</p>
    <p>Lorem ipsum dolor sit amet, consectetur adipiscing elit. Nunc bibendum ultricies mi. Duis ac ligula lorem. Nunc ac dui dignissim, facilisis libero sed, posuere mi. Donec suscipit elementum odio. Sed elementum leo diam, a imperdiet quam lobortis nec. Nunc dictum malesuada mi, sed hendrerit lacus aliquet dictum. In iaculis augue at cursus consectetur lis sapien vitae ligula volutpat efficitur. Aliquam quis quam eget ligula sagittis congue.</p>
    <p>Nam mollis ipsum sapien, vehicula fringilla erat fermentum id. Aenean nec feugiat ex. Nunc imperdiet non ligula vitae aliquet. Aliquam pellentesque nec ligula sit amet blandit. Integer vitae aliquet ante. Proin tempor auctor etus ac augue porttitor ornare id et arcu. Aliquam erat volutpat. Nullam convallis sapien vitae ligissim, facilisis libero sed, posuere mi. Donec suscipit elementum odio. Sed elementum leo diam, a imperdiet quam lobortis necunc malesuada mised.</p>
  </div>
  <div class="sign-off">Sincerely,<br>Managing Director</div>

  <div class="contact-row">
    <span><svg viewBox="0 0 10 10" aria-hidden="true"><path d="M2 1h2l1 2.5-1.3 1A6 6 0 0 0 5.5 6.3l1-1.3L9 6v2a1 1 0 0 1-1 1A7 7 0 0 1 1 2a1 1 0 0 1 1-1z" fill="var(--brand-green)"/></svg>P. +555-284-6103</span>
    <span><i></i>brent@brentoakesstudio-mail.net</span>
    <span><i></i>brentoakesstudio-mail.net</span>
  </div>
</section>

</body>
</html>
```